Stationary Package for New Bookkeeping Business

We need the following stationary designs:

- Business Card
- Letterhead
- With Comps
- Envelopes
- Paper Folder
- Email Signature

We will provide accounting and bookkeeping services to small business. We would like have the main color as blue and have a modern professional look.

Variations of colour and shades of blue welcome
Preference for deeper darker blue - navy

Variations of font in logo also welcome

Industry/Entity Type

Accounting

Requirements
Must have
• Rosalind
B.Bus (Accounting)
Registered BAS Agent

Phone 0491 382 207
Post PO Box 624 Wattlegrove NSW 2749

Email rosalind@corbettledger.com

Business Card to be bold and eye catching

Should not have
• Letter head to not have too much colour on it

```html
<!DOCTYPE html>
<html lang="en">
<head>
<meta charset="utf-8">
<title>Corbett Ledger — Stationery Suite</title>
<link href="https://fonts.googleapis.com/css2?family=Roboto:wght@400;500;700&display=swap" rel="stylesheet">
<style>
  :root {
    --bg: #ececec;
    --paper: #ffffff;
    --paper-shade: #f4f4f4;
    --brand-blue: #2f72b8;
    --folder-blue: #4a88c4;
    --folder-deep: #3a76b4;
    --folder-light: #5291cb;
    --flap-blue: #0b69bb;
    --mark-grey: #9a9a9a;
    --rule-grey: #a9a9a9;
    --ink: #555555;
  }
  * { box-sizing: border-box; margin: 0; padding: 0; }
  html, body { width: 1200px; height: 800px; overflow: hidden; }
  body {
    background: var(--bg);
    font-family: "Roboto", Arial, sans-serif;
    position: relative;
  }
  .piece { position: absolute; }

  /* Brand lockup: square + name, one colour, one weight */
  .lockup { display: flex; align-items: center; gap: 6px; font-weight: 500; line-height: 1; position: relative; z-index: 2; }
  .lockup__square { background: var(--mark-grey); flex: none; }
  .lockup__name { display: flex; flex-direction: column; }
  .lockup--blue .lockup__name { color: var(--brand-blue); }
  .lockup--white .lockup__name { color: var(--paper); }
  .lockup--white .lockup__square { background: var(--paper); }

  /* Decorative pattern area, shown as soft tonal field */
  .pattern-field {
    position: absolute; inset: 0; z-index: 1;
    background:
      radial-gradient(ellipse at 30% 20%, var(--folder-deep) 0%, transparent 45%),
      radial-gradient(ellipse at 70% 85%, var(--folder-deep) 0%, transparent 45%),
      linear-gradient(135deg, var(--folder-light), var(--folder-blue) 50%, var(--folder-light));
  }

  /* Letterhead */
  .letterhead {
    left: 95px; top: 98px; width: 307px; height: 432px;
    background: var(--paper);
  }
  .letterhead__top-rule { position: absolute; left: 0; top: 0; width: 284px; height: 5px; background: var(--rule-grey); }
  .letterhead__top-accent { position: absolute; left: 291px; top: 0; width: 16px; height: 5px; background: var(--brand-blue); }
  .letterhead__side-rule { position: absolute; right: 0; top: 5px; width: 3px; height: 427px; background: var(--paper-shade); }
  .letterhead .lockup { position: absolute; left: 13px; top: 20px; font-size: 14px; gap: 5px; }
  .letterhead .lockup__square { width: 26px; height: 26px; }
  .letterhead__footer {
    position: absolute; left: 20px; right: 0; bottom: 0; height: 5px; background: var(--brand-blue);
  }
  .letterhead__footer-grey { position: absolute; left: 0; bottom: 0; width: 8px; height: 5px; background: var(--rule-grey); }
  .letterhead__address {
    position: absolute; left: 0; right: 0; bottom: 8px; text-align: center;
    font-size: 7px; letter-spacing: 0.6px; color: var(--brand-blue); font-weight: 500;
  }

  /* Folders */
  .folder {
    left: 432px; top: 98px; width: 307px; height: 432px;
    background: var(--folder-blue);
    display: flex; align-items: center; justify-content: center;
  }
  .folder .lockup { font-size: 17px; gap: 8px; }
  .folder .lockup__square { width: 34px; height: 34px; }
  .folder-open {
    left: 780px; top: 72px; width: 335px; height: 463px;
    background: var(--folder-blue);
    display: flex; align-items: center; justify-content: center;
  }
  .folder-open__spine { position: absolute; left: 0; top: 0; width: 8px; height: 100%; background: var(--folder-deep); opacity: .6; z-index: 2; }
  .folder-open__edge { position: absolute; left: 274px; top: 0; width: 2px; height: 100%; background: var(--paper); z-index: 2; }
  .folder-open .lockup { font-size: 16px; gap: 8px; margin-right: 66px; }
  .folder-open .lockup__square { width: 32px; height: 32px; }

  /* With compliments slip */
  .comp-slip {
    left: 88px; top: 563px; width: 315px; height: 160px;
    background: var(--paper);
  }
  .comp-slip .lockup { position: absolute; left: 10px; top: 10px; font-size: 11px; gap: 4px; }
  .comp-slip .lockup__square { width: 18px; height: 18px; }
  .comp-slip__corner { position: absolute; left: 0; bottom: 0; width: 32px; height: 24px; background: var(--mark-grey); }
  .comp-slip__band {
    position: absolute; left: 32px; right: 0; bottom: 0; height: 10px; background: var(--brand-blue);
    color: var(--paper); font-size: 6.5px; font-weight: 500; letter-spacing: 0.6px;
    display: flex; align-items: center; justify-content: center;
  }

  /* Envelope */
  .envelope { left: 435px; top: 562px; width: 320px; height: 160px; }
  .envelope svg { display: block; }

  /* Business cards */
  .card { width: 132px; height: 75px; }
  .card--front { left: 793px; top: 560px; background: var(--paper); }
  .card--front .lockup { position: absolute; left: 6px; top: 8px; font-size: 6.5px; gap: 3px; }
  .card--front .lockup__square { width: 12px; height: 12px; }
  .card__name-band {
    position: absolute; left: 46px; right: 0; top: 21px; height: 11px; background: var(--brand-blue);
    color: var(--paper); font-size: 8px; font-weight: 700; letter-spacing: 0.8px;
    display: flex; align-items: center; justify-content: flex-end; padding-right: 6px;
  }
  .card__credentials {
    position: absolute; right: 6px; top: 34px; text-align: right;
    font-size: 4.2px; line-height: 1.35; color: var(--ink); letter-spacing: 0.2px;
  }
  .card__contact {
    position: absolute; left: 6px; top: 54px; font-size: 3.6px; line-height: 1.4; color: var(--ink);
    white-space: nowrap;
  }
  .card__contact b { color: var(--brand-blue); font-weight: 500; }
  .card--back {
    left: 978px; top: 560px; background: var(--folder-blue); overflow: hidden;
    display: flex; align-items: center; justify-content: center;
  }
  .card--back .lockup { font-size: 8px; gap: 4px; }
  .card--back .lockup__square { width: 14px; height: 14px; }
</style>
</head>
<body>

  <section class="piece letterhead" aria-label="Letterhead">
    <div class="letterhead__top-rule"></div>
    <div class="letterhead__top-accent"></div>
    <div class="letterhead__side-rule"></div>
    <div class="lockup lockup--blue">
      <span class="lockup__square"></span>
      <span class="lockup__name"><span>Corbett</span><span>Ledger</span></span>
    </div>
    <p class="letterhead__address">POST PO BOX 624 WATTLEGROVE NSW 2749</p>
    <div class="letterhead__footer-grey"></div>
    <div class="letterhead__footer"></div>
  </section>

  <section class="piece folder" aria-label="Presentation folder, front">
    <div class="pattern-field" role="img" aria-label="Large tonal pattern of accounting symbols and crossing diagonal bands"></div>
    <div class="lockup lockup--white">
      <span class="lockup__square"></span>
      <span class="lockup__name"><span>Corbett</span><span>Ledger</span></span>
    </div>
  </section>

  <section class="piece folder-open" aria-label="Presentation folder, with pocket flap">
    <div class="pattern-field" role="img" aria-label="Large tonal pattern of accounting symbols and crossing diagonal bands"></div>
    <div class="folder-open__spine"></div>
    <div class="folder-open__edge"></div>
    <div class="lockup lockup--white">
      <span class="lockup__square"></span>
      <span class="lockup__name"><span>Corbett</span><span>Ledger</span></span>
    </div>
  </section>

  <section class="piece comp-slip" aria-label="With compliments slip">
    <div class="lockup lockup--blue">
      <span class="lockup__square"></span>
      <span class="lockup__name"><span>Corbett</span><span>Ledger</span></span>
    </div>
    <div class="comp-slip__corner"></div>
    <div class="comp-slip__band">POST PO BOX 624 WATTLEGROVE NSW 2749</div>
  </section>

  <section class="piece envelope" aria-label="DL envelope, back with open flap">
    <svg width="320" height="160" viewBox="0 0 320 160">
      <rect x="0" y="0" width="320" height="160" fill="var(--paper)"/>
      <path d="M0 0 H320 V22 Q320 38 304 38 H16 Q0 38 0 22 Z" fill="var(--flap-blue)"/>
      <path d="M0 38 L150 100 H170 L320 38" fill="none" stroke="var(--paper-shade)" stroke-width="1.5"/>
    </svg>
  </section>

  <section class="piece card card--front" aria-label="Business card, front">
    <div class="lockup lockup--blue">
      <span class="lockup__square"></span>
      <span class="lockup__name"><span>Corbett</span><span>Ledger</span></span>
    </div>
    <div class="card__name-band">ROSALIND</div>
    <div class="card__credentials">
      <p>B.BUS (ACCOUNTING)</p>
      <p>Registered BAS Agent</p>
    </div>
    <div class="card__contact">
      <p><b>PHONE</b> 0491 382 207</p>
      <p><b>POST</b> PO BOX 624 WATTLEGROVE NSW 2749</p>
      <p><b>Email</b> rosalind@corbettledger.com</p>
    </div>
  </section>

  <section class="piece card card--back" aria-label="Business card, back">
    <div class="pattern-field" role="img" aria-label="Tonal pattern of accounting symbols and crossing diagonal bands"></div>
    <div class="lockup lockup--white">
      <span class="lockup__square"></span>
      <span class="lockup__name"><span>Corbett</span><span>Ledger</span></span>
    </div>
  </section>

</body>
</html>
```